3D Printing Website redesign

We are in the process of redesigning our website. Attached is an image of one of the proposed pages - "The Brightlander". The idea with this page is that site visitors can get an indicative estimate of the cost of 3D Printing based on some provided metrics. When the user alters the metrics the price changes accordingly. We are looking for a design to support this page that will also be used across our site.

```html
<!DOCTYPE html>
<html lang="en">
<head>
<meta charset="utf-8">
<title>Layerform Studio – The Brightlander</title>
<link href="https://fonts.googleapis.com/css2?family=Maven+Pro:wght@400;500;700&family=Open+Sans:wght@400;600;700&display=swap" rel="stylesheet">
<style>
:root{
  --blue:#1679c7;
  --blue-deep:#0b4f99;
  --blue-dark:#0a3d7a;
  --navy:#0d3b72;
  --link:#1a5fa8;
  --grey-bg:#efefef;
  --grey-line:#cfcfcf;
  --text:#666;
  --text-dark:#444;
  --footer:#3d4145;
  --footer-dark:#232527;
  --white:#fff;
  --orange:#ea7a45;
  --submit:#0aa0e4;
}
*{margin:0;padding:0;box-sizing:border-box}
html,body{width:1024px;height:1200px;overflow:hidden}
body{position:relative;background:var(--white);font-family:"Open Sans",sans-serif;color:var(--text)}
.abs{position:absolute}
/* header */
.topbar{left:0;top:0;width:1024px;height:8px;background:#cfd4d8}
.account-tab{left:744px;top:0;width:136px;height:18px;background:#cfd4d8;border-radius:0 0 6px 6px;font:500 9px "Maven Pro",sans-serif;color:var(--link);display:flex;justify-content:center;gap:16px;align-items:center}
.brand{left:140px;top:22px;display:flex;align-items:center;gap:10px}
.brand-mark{width:64px;height:64px;border-radius:50%;background:#2b6fb5}
.brand-name{font:700 22px "Maven Pro",sans-serif;color:var(--link)}
.social-top{top:31px;width:19px;height:19px;border-radius:50%;background:var(--link)}
.call{left:686px;top:32px;width:18px;height:18px;background:var(--navy);border-radius:3px}
.call-text{left:710px;top:33px;font:400 13px "Maven Pro",sans-serif;color:#888}
.call-text b{color:var(--link);font-weight:700}
.nav{left:430px;top:64px;width:456px;display:flex;justify-content:space-between;font:400 11px "Maven Pro",sans-serif;color:#777}
.nav span.sep{color:#aaa}
.nav .active{color:var(--link)}
.nav-pointer{left:585px;top:94px;width:0;height:0;border-left:9px solid transparent;border-right:9px solid transparent;border-bottom:10px solid var(--blue)}
/* hero */
.hero{left:0;top:104px;width:1024px;height:392px;background:linear-gradient(180deg,#1c82cf 0%,#0f62b2 100%)}
.hero-art{left:0;top:104px;width:346px;height:370px;background:radial-gradient(ellipse at 60% 35%,#2f8fdc 0%,#0c57a8 55%,rgba(10,70,140,0) 80%)}
.action{left:136px;width:192px;height:58px;background:linear-gradient(#fff,#e8e8e8);border-radius:3px;box-shadow:0 2px 0 #b9c3cc;display:flex;align-items:center;justify-content:center;gap:12px;font:400 25px "Maven Pro",sans-serif;color:#707880}
.action svg{width:24px;height:24px;fill:#707880}
.quote-title{left:362px;top:122px;width:320px;text-align:center;font:400 24px "Maven Pro",sans-serif;color:var(--white)}
.metric-label{left:393px;font:500 13px "Maven Pro",sans-serif;color:var(--white)}
.slider{left:393px;width:239px;height:6px;border-radius:3px;background:linear-gradient(90deg,#3b3f44 0 59%,#e9eef2 59% 100%)}
.thumb{left:528px;width:13px;height:13px;border-radius:50%;background:#fff;border:2px solid #c5ccd3}
.scale{font:400 10px "Maven Pro",sans-serif;color:#a9cdeb;top:231px}
.select{left:392px;top:416px;width:238px;height:32px;background:#f5f5f5;border-radius:3px;font:400 14px "Maven Pro",sans-serif;color:#666;padding:8px 10px}
.select .divider{position:absolute;right:34px;top:6px;height:20px;border-left:1px solid #ddd}
.select svg{position:absolute;right:10px;top:11px}
.preview{left:695px;top:173px;width:193px;height:193px;border-radius:50%;background:rgba(140,190,225,.35);border:1px solid #5ba0d6}
.total{left:696px;top:417px;width:192px;height:32px;background:var(--navy);color:#fff;font:500 14px "Maven Pro",sans-serif;display:flex;align-items:center;justify-content:center}
/* form */
.inquiry{left:0;top:496px;width:1024px;height:430px;background:var(--grey-bg)}
.inquiry-title{left:0;top:527px;width:1020px;text-align:center;font:400 17.5px "Open Sans",sans-serif;color:#777}
.field-label{left:260px;font-size:9.5px;color:#666}
.field{left:259px;width:245px;background:#fff;border:1px solid var(--grey-line)}
.field.focus{border-color:var(--orange)}
.field svg{position:absolute;left:9px;top:8px}
.field .tick{position:absolute;left:32px;top:6px;height:17px;border-left:1px dotted #ccc}
.captcha{left:521px;top:588px;width:239px;height:94px;background:#fff;border:1px solid #ddd;border-radius:4px}
.captcha-word{left:0;top:0;width:237px;height:65px;background:linear-gradient(#fff,#f4f4f4)}
.captcha-bar{left:0;top:65px;width:237px;height:28px;border-top:1px solid #e4e4e4;display:flex}
.captcha-bar .hint{width:147px;font:600 9px "Open Sans",sans-serif;color:#555;padding:8px 0 0 23px;border-right:1px solid #e4e4e4}
.captcha-bar .tool{width:30px;border-right:1px solid #e4e4e4;display:flex;align-items:center;justify-content:center}
.check{left:524px;top:780px;width:14px;height:14px;background:#ddd;border:1px solid #ccc;border-radius:2px}
.check-text{left:550px;top:781px;font-size:9.5px;color:#666}
.submit{left:519px;top:820px;width:246px;height:39px;background:linear-gradient(#12b1f1,#0889d0);border-bottom:3px solid #0a4d88;border-radius:2px;color:#fff;font:700 14px "Open Sans",sans-serif;display:flex;align-items:center;justify-content:center}
.note{left:258px;top:879px;width:504px;text-align:center;font-size:9.5px;line-height:14.5px;color:#888}
/* footer */
.footer{left:0;top:926px;width:1024px;height:240px;background:linear-gradient(#4a4e52,#2f3235);border-top:2px solid #2a2c2e}
.col-title{font:700 12.5px "Open Sans",sans-serif;color:#fff;padding-bottom:6px;border-bottom:1px solid #5a5e62}
.col-text{font-size:10px;line-height:14.4px;color:#e8e8e8}
.contact-row{left:394px;display:flex;gap:14px;align-items:center;font-size:10px;color:#fff}
.contact-row svg{width:14px;height:14px;fill:#8a8f94}
.sub-input{left:648px;top:1022px;width:238px;height:30px;background:#6f767c;border:1px solid #595e62}
.sub-btn{left:822px;top:1023px;width:63px;height:28px;background:#4b5e74;color:#fff;font:700 9.5px "Open Sans",sans-serif;display:flex;align-items:center;justify-content:center}
.social-sq{top:1100px;width:27px;height:27px;border-radius:3px}
.bottom{left:0;top:1166px;width:1024px;height:34px;background:var(--footer-dark);font-size:8.5px;color:#9a9ea2}
</style>
</head>
<body>
<header>
  <div class="abs topbar"></div>
  <div class="abs account-tab"><span>Login</span><span>Register</span></div>
  <div class="abs brand"><div class="brand-mark"></div><div class="brand-name">Layerform Studio</div></div>
  <div class="abs social-top" style="left:593px" aria-label="Social profile 1"></div>
  <div class="abs social-top" style="left:621px" aria-label="Social profile 2"></div>
  <div class="abs social-top" style="left:649px" aria-label="Social profile 3"></div>
  <div class="abs call"><svg width="18" height="18" viewBox="0 0 18 18"><path d="M5 4c1 0 2 2 2 3s-1 1-1 2 2 3 3 3 1-1 2-1 3 1 3 2-1 2-2 2C7 15 3 11 3 6c0-1 1-2 2-2z" fill="#fff"/></svg></div>
  <div class="abs call-text">Call us today <b>+1800.555.0147</b></div>
  <nav class="abs nav">
    <span>Shop</span><span class="sep">|</span><span>What We Do</span><span class="sep">|</span><span class="active">Pricing &amp; Quote</span><span class="sep">|</span><span>Gallery</span><span class="sep">|</span><span>DIY</span><span class="sep">|</span><span>Training</span><span class="sep">|</span><span>Blog</span><span class="sep">|</span><span>Contact Us</span>
  </nav>
  <div class="abs nav-pointer"></div>
</header>

<section>
  <div class="abs hero"></div>
  <div class="abs hero-art" role="img" aria-label="Large glossy blue 3D printed abstract sculpture"></div>
  <div class="abs action" style="top:188px"><svg viewBox="0 0 24 24"><path d="M6 2h12v5H6zM3 8h18a1 1 0 0 1 1 1v8h-4v5H6v-5H2V9a1 1 0 0 1 1-1zm5 8v4h8v-4z"/></svg>Print</div>
  <div class="abs action" style="top:268px"><svg viewBox="0 0 24 24"><path d="M11 1h2v5h-2zM11 18h2v5h-2zM1 11h5v2H1zM18 11h5v2h-5z"/><circle cx="12" cy="12" r="7" fill="none" stroke="#707880" stroke-width="2"/></svg>Scan</div>
  <div class="abs action" style="top:347px"><svg viewBox="0 0 24 24"><path d="M3 5h10v2H5v12h12v-7h2v9H3z"/><path d="M19 2l3 3-10 10H9v-3z"/></svg>Design</div>

  <h1 class="abs quote-title">Get Instant Quote or</h1>
  <div class="abs metric-label" style="top:185px">SHAPE</div>
  <div class="abs slider" style="top:217px"></div><div class="abs thumb" style="top:213px"></div>
  <div class="abs scale" style="left:393px">Square</div><div class="abs scale" style="left:593px">Circular</div>
  <div class="abs metric-label" style="top:264px">SIZE</div>
  <div class="abs slider" style="top:296px"></div><div class="abs thumb" style="top:292px"></div>
  <div class="abs metric-label" style="top:344px">VOLUME</div>
  <div class="abs slider" style="top:376px"></div><div class="abs thumb" style="top:372px"></div>
  <div class="abs select">Material<span class="divider"></span><svg width="12" height="8" viewBox="0 0 12 8"><path d="M1 1l5 5 5-5" stroke="#666" stroke-width="2" fill="none"/></svg></div>
  <div class="abs preview"></div>
  <div class="abs total">Brightlander Total: $360</div>
</section>

<section>
  <div class="abs inquiry"></div>
  <h2 class="abs inquiry-title" style="font-weight:400">For further information and inquiries, please fill the form below:</h2>
  <div class="abs field-label" style="top:570px">Your Name</div>
  <div class="abs field focus" style="top:588px;height:30px"><svg width="14" height="14" viewBox="0 0 14 14"><circle cx="7" cy="4" r="3" fill="#c8c8c8"/><path d="M1 14c0-4 3-6 6-6s6 2 6 6z" fill="#c8c8c8"/></svg><span class="tick"></span></div>
  <div class="abs field-label" style="top:632px">Your Phone Number</div>
  <div class="abs field" style="top:653px;height:30px"><svg width="14" height="14" viewBox="0 0 14 14"><path d="M3 1c1 0 2 2 2 3s-1 1-1 2 2 3 3 3 1-1 2-1 3 1 3 2-1 2-2 2C5 12 1 8 1 3c0-1 1-2 2-2z" fill="#c8c8c8"/></svg><span class="tick"></span></div>
  <div class="abs field-label" style="top:695px">Your Email Address</div>
  <div class="abs field" style="top:714px;height:30px"><svg width="16" height="12" viewBox="0 0 16 12"><rect width="16" height="12" fill="#c8c8c8"/><path d="M0 0l8 6 8-6" stroke="#fff" fill="none"/></svg><span class="tick"></span></div>
  <div class="abs field-label" style="top:757px">Instructions</div>
  <div class="abs field" style="top:777px;height:86px"><svg width="14" height="12" viewBox="0 0 14 12"><ellipse cx="7" cy="5" rx="7" ry="5" fill="#c8c8c8"/><path d="M2 8l-1 4 4-3z" fill="#c8c8c8"/></svg><span class="tick"></span></div>

  <div class="abs captcha">
    <div class="abs captcha-word" role="img" aria-label="Distorted verification word"></div>
    <div class="abs captcha-bar">
      <div class="hint">Type the above code</div>
      <div class="tool"><svg width="11" height="11" viewBox="0 0 12 12"><path d="M10 4A4.5 4.5 0 1 0 10.5 8" stroke="#555" stroke-width="1.6" fill="none"/><path d="M8 1l3 3-3 1z" fill="#555"/></svg></div>
      <div class="tool"><svg width="12" height="10" viewBox="0 0 12 10"><path d="M0 3h3l4-3v10L3 7H0z" fill="#555"/><path d="M9 2q2 3 0 6" stroke="#555" fill="none"/></svg></div>
      <div class="tool" style="border-right:0"><svg width="11" height="11" viewBox="0 0 12 12"><circle cx="6" cy="6" r="6" fill="#555"/><rect x="5.2" y="2.5" width="1.6" height="4.5" fill="#fff"/><rect x="5.2" y="8" width="1.6" height="1.6" fill="#fff"/></svg></div>
    </div>
  </div>
  <div class="abs check"><svg width="12" height="12" viewBox="0 0 12 12"><path d="M2 6l3 3 5-7" stroke="#444" stroke-width="2" fill="none"/></svg></div>
  <div class="abs check-text">I would like to receive promotional material.</div>
  <div class="abs submit">SUBMIT FORM</div>
  <p class="abs note">*Price is indicative only and may be subject ot change. An accurate estimate will be provided upon receiving a print-ready 3D design file.</p>
</section>

<footer>
  <div class="abs footer"></div>
  <div class="abs" style="left:138px;top:952px;width:170px">
    <div class="col-title">About Us</div>
    <p class="col-text" style="margin-top:11px">Duis mollis, est non commodo luctus, nisi erat porttitor ligula, eget lacinia odio sem nec elit. Vestibu-lum id ligula porta felis euismod semper. Integer posuere erat a ante.</p>
    <p class="col-text" style="margin-top:14px">Vestibulum id ligula porta felis euismod semper. Integer posuere erat a ante.</p>
  </div>
  <div class="abs" style="left:394px;top:952px;width:170px">
    <div class="col-title">Contact Details</div>
    <p class="col-text" style="margin-top:11px">There are many variations of pas-sages of Lorem Ipsum available, but the majority have suffered altera-tion.</p>
  </div>
  <div class="abs contact-row" style="top:1066px"><svg viewBox="0 0 14 14"><path d="M7 0a5 5 0 0 1 5 5c0 4-5 9-5 9S2 9 2 5a5 5 0 0 1 5-5z"/><circle cx="7" cy="5" r="2" fill="#3d4145"/></svg>Harbor City</div>
  <div class="abs contact-row" style="top:1090px"><svg viewBox="0 0 14 14"><rect y="2" width="14" height="10"/><path d="M0 2l7 5 7-5" stroke="#3d4145" fill="none"/></svg>info@layerform-example.com</div>
  <div class="abs contact-row" style="top:1114px"><svg viewBox="0 0 14 14"><path d="M3 1c1 0 2 2 2 3s-1 1-1 2 2 3 3 3 1-1 2-1 3 1 3 2-1 2-2 2C5 12 1 8 1 3c0-1 1-2 2-2z"/></svg>890-55501-23456</div>
  <div class="abs" style="left:648px;top:951px;width:240px">
    <div class="col-title">Newsletter Signup</div>
    <p class="col-text" style="margin-top:11px;color:#c9cdd1">By subscribing to our mailing list you will get the latest news from us.</p>
  </div>
  <div class="abs sub-input"></div>
  <div class="abs sub-btn">Subscribe</div>
  <div class="abs col-title" style="left:650px;top:1070px;border:0">Get Social</div>
  <div class="abs social-sq" style="left:649px;background:#3b5b99" aria-label="Social profile 1"></div>
  <div class="abs social-sq" style="left:685px;background:#2f9ee0" aria-label="Social profile 2"></div>
  <div class="abs social-sq" style="left:721px;background:#1b76a8" aria-label="Social profile 3"></div>
  <div class="abs social-sq" style="left:757px;background:#d03a2c" aria-label="Social profile 4"></div>
  <div class="abs bottom">
    <span class="abs" style="left:135px;top:12px">Copyright 2014 © Layerform Studio - All Rights Reserved</span>
    <span class="abs" style="left:787px;top:12px">Site Map &nbsp;&nbsp;•&nbsp;&nbsp; Privacy Policy</span>
  </div>
</footer>
</body>
</html>
```